ZestLoop.Com Website Design
New Social Media Platform
ZestLoop.Com Website Design - Social Media
Creative Brief
Social Media
www.zestloop.com (you may login in as username=guest, password=guest) Sorry but the site is slow.
ZestLoop.com is a website that lets users respond to things they like on the internet by using sounds. Sounds will be registered in a real-time window in the user's browser - kind of like chirplet but with sound. User's can respond to 'Bumper Stickers' posted on the website and those they "honk" at will cause a sound to be registered on the computers of all people connected to the site. A "Honk" button will also be able to be embedded on any web page - like the VR "Like" or chirplet "tweet" button - and will cause a sound to be registered in the same manner.
I would rather not cloud any creative thinking by stating my likes and dislikes, but, I think this site should have a "fun" feel without being too whimsical or silly.
Fun
See Logo File for Colors
Arial, Verdana, Trebuchet MS, Century Gothic, Georgia
above header
www.quillmarket.com
dating.quillmarket.com
chirplet/snapboard
There are a few files uploaded which show the rough site that I have put together so far. Right now the website lends itself to 2 scrolling windows: 1 which displays "bumper stickers" that scroll by (like in dating.quillmarket.com - you can see this by following the first dialog box to create a free account without actually having to create one) and a second window that shows people "honking" (like a chirplet window that shows tweets). I am open to other suggestions for how to display the "bumper stickers" portion. The design requires the web template and also a "Honk" button that can be embedded into a web page (like chirplet "tweet" button"). Please feel free to contact me with any questions. A prototype version of the website is running at www.zestloop.com. Sorry but the site is slow as it is running on a slow server and connection, but feel free to check it out.

```html
<!DOCTYPE html>
<html lang="en">
<head>
<meta charset="utf-8">
<title>ZestLoop.Com</title>
<link href="https://fonts.googleapis.com/css2?family=Arimo:ital,wght@0,400;0,700;1,400&display=swap" rel="stylesheet">
<style>
:root{
  --navy:#1b3347;
  --navy-dark:#12283a;
  --blue:#1a9ad6;
  --blue-light:#3bb4e8;
  --blue-text:#1578b8;
  --red:#d9432f;
  --red-dark:#b5311f;
  --deep:#174e6e;
  --ink:#2c3e50;
  --muted:#9aa5ad;
  --line:#e1e6ea;
  --page:#f1f3f5;
  --white:#ffffff;
  --strip:#e9ecef;
}
*{box-sizing:border-box;margin:0;padding:0}
html,body{width:1200px;height:927px;overflow:hidden}
body{font-family:"Arimo",Arial,sans-serif;color:var(--ink);background:linear-gradient(#fafbfc,var(--page) 60%,#e8ebee);position:relative}
.topnav{position:absolute;left:0;top:0;width:1200px;height:25px;background:var(--navy)}
.topnav .inner{position:absolute;left:195px;width:812px;height:25px;display:flex;font-size:10px;font-weight:700;text-transform:uppercase;color:#dfe7ee}
.topnav a{display:block;padding:0 14px;line-height:25px;color:inherit;text-decoration:none}
.topnav a.active{background:var(--blue);color:var(--white)}
.topnav .account{margin-left:auto;display:flex}
.topnav .register{background:var(--red)}
.topnav .login{background:var(--red-dark)}
.tips{position:absolute;left:0;top:25px;width:1200px;height:26px;background:#f7f9fa;border-bottom:1px solid var(--line)}
.tips p{position:absolute;left:195px;line-height:26px;font-size:10px;color:var(--muted)}
.tips strong{color:var(--blue-text);margin-right:12px;text-transform:uppercase}
.brand{position:absolute;left:198px;top:100px;display:flex;align-items:center;gap:10px;font-size:44px;font-weight:700;color:var(--blue)}
.brand .dot{width:22px;height:22px;border-radius:50%;background:var(--deep)}
.tagline{position:absolute;left:591px;top:100px;width:416px;height:60px;background:var(--white);border:1px solid var(--line);padding-left:18px;line-height:58px;font-size:19px;color:var(--blue-text)}
.tagline b{color:var(--deep)}
.feed{position:absolute;left:195px;top:208px;width:545px}
.post{position:relative;height:113px;margin-bottom:12px;background:var(--white);border:1px solid var(--line)}
.post .avatar{position:absolute;left:8px;top:10px;width:44px;height:80px;background:linear-gradient(#f5f7f8,#e6eaed);border:1px solid var(--line)}
.post .avatar.male::after,.post .avatar.female::after{content:"";position:absolute;left:14px;top:12px;width:16px;height:56px;border-radius:3px;background:var(--deep)}
.post .avatar.female::after{background:var(--red)}
.post .title{position:absolute;left:68px;top:12px;font-size:10px;color:var(--blue-text)}
.post .time{position:absolute;left:330px;top:12px;font-size:10px;color:var(--muted);display:flex;gap:18px}
.post .text{position:absolute;left:68px;top:32px;width:330px;font-size:15px;line-height:19px;color:var(--deep)}
.post .meta{position:absolute;left:68px;top:82px;font-size:9px;color:var(--muted);display:flex;gap:22px}
.post .honk{position:absolute;right:0;top:0;width:75px;height:111px;background:var(--strip);display:flex;align-items:center;justify-content:center}
.post .honk span{width:30px;height:30px;border-radius:50%;border:3px solid #c7cfd5}
.post.active{border-color:#c6d3dc}
.post.active .honk{background:var(--white)}
.post.active .honk span{border-color:var(--blue)}
.sidebar{position:absolute;left:767px;top:208px;width:240px}
.panel-head{height:45px;background:linear-gradient(var(--blue-light),var(--blue));color:var(--white);font-size:14px;line-height:45px;padding-left:22px;text-transform:uppercase}
.signin{background:var(--white);border:1px solid var(--line);border-top:0;height:290px;position:relative}
.signin .field{position:absolute;left:12px;width:216px;height:28px;border:1px solid var(--line);background:#fafbfc;font-size:11px;color:var(--muted);text-align:right;padding-right:12px;line-height:26px}
.signin .btn{position:absolute;top:162px;height:38px;line-height:38px;font-size:11px;font-weight:700;color:var(--white);text-align:center}
.signin .btn.login{left:12px;width:88px;background:var(--red)}
.signin .btn.reg{left:136px;width:92px;background:var(--deep)}
.signin .or{position:absolute;left:111px;top:174px;font-size:10px;color:var(--muted)}
.signin .remember{position:absolute;left:12px;top:222px;font-size:9px;color:var(--muted)}
.signin .forgot{position:absolute;right:12px;top:264px;font-size:10px;color:var(--deep)}
.honking{margin-top:20px}
.honking ul{list-style:none;background:var(--white);border:1px solid var(--line);border-top:0;padding:6px 10px}
.honking li{display:flex;gap:10px;padding:9px 0;border-bottom:1px solid var(--line)}
.honking li:last-child{border-bottom:0}
.honking .mini{width:28px;height:28px;flex:none;background:#dde4e9;border:1px solid #c9d3da}
.honking small{display:block;font-size:9px;color:var(--muted)}
.honking small b{color:var(--blue-text)}
.honking p{font-size:13px;color:var(--deep)}
.footer{position:absolute;left:0;top:882px;width:1200px;height:45px;background:var(--blue);color:#dff2fb;font-size:10px;text-align:center;line-height:45px}
</style>
</head>
<body>
<nav class="topnav"><div class="inner">
  <a class="active">Home</a><a>My Bumper Stickers</a><a>Embed Honk Button</a>
  <div class="account"><a class="register">Register</a><a class="login">Log In ▾</a></div>
</div></nav>
<div class="tips"><p><strong>Honkin' Tips</strong>Site requires use of ReelTime Player - you might have to download it.</p></div>

<div class="brand"><span>ZestLoop</span><span class="dot"></span></div>
<div class="tagline">Honk if you like <b>Beautiful Design!</b></div>

<main class="feed">
  <article class="post">
    <div class="avatar male" role="img" aria-label="Man icon"></div>
    <div class="title">Honk if you like</div><div class="time"><span>1 hour</span><span>1 minute</span></div>
    <p class="text">A good coffee in the morning and a <b>beautiful</b>, sweet girl in the evening</p>
    <div class="meta"><span>JEFF</span><span>3/16/11</span><span>1,230</span><span>Follow</span></div>
    <div class="honk"><span></span></div>
  </article>
  <article class="post">
    <div class="avatar female" role="img" aria-label="Woman icon"></div>
    <div class="title">Honk if you like</div><div class="time"><span>1 hour</span><span>1 minute</span></div>
    <p class="text">A good coffee <i>in the morning</i> and a beautiful, sweet girl in the evening</p>
    <div class="meta"><span>ANN</span><span>3/16/11</span><span>1,230</span><span>Follow</span></div>
    <div class="honk"><span></span></div>
  </article>
  <article class="post active">
    <div class="avatar male" role="img" aria-label="Man icon"></div>
    <div class="title">Honk if you like</div><div class="time"><span>1 hour</span><span>1 minute</span></div>
    <p class="text">A good coffee in the morning and a beautiful, sweet girl in the evening</p>
    <div class="meta"><span>JEFF</span><span>3/16/11</span><span>1,230</span><span>Follow</span></div>
    <div class="honk"><span></span></div>
  </article>
  <article class="post">
    <div class="avatar female" role="img" aria-label="Woman icon"></div>
    <div class="title">Honk if you like</div><div class="time"><span>1 hour</span><span>1 minute</span></div>
    <p class="text"><b>A good coffee</b> in the morning and a beautiful, sweet girl in the evening</p>
    <div class="meta"><span>ANN</span><span>3/16/11</span><span>1,230</span><span>Follow</span></div>
    <div class="honk"><span></span></div>
  </article>
  <article class="post">
    <div class="avatar male" role="img" aria-label="Man icon"></div>
    <div class="title">Honk if you like</div><div class="time"><span>1 hour</span><span>1 minute</span></div>
    <p class="text">A good coffee in the morning and a beautiful, sweet girl in the evening</p>
    <div class="meta"><span>JEFF</span><span>3/16/11</span><span>1,230</span><span>Follow</span></div>
    <div class="honk"><span></span></div>
  </article>
</main>

<aside class="sidebar">
  <section>
    <div class="panel-head">Sign in to <b>ZestLoop</b></div>
    <div class="signin">
      <div class="field" style="top:15px">username or email</div>
      <div class="field" style="top:57px">password</div>
      <div class="btn login">LOG-IN</div><span class="or">or</span><div class="btn reg">REGISTER</div>
      <div class="remember">☐ Remember Me</div>
      <div class="forgot">Forgot Your Password?</div>
    </div>
  </section>
  <section class="honking">
    <div class="panel-head">People <b>Honking</b></div>
    <ul>
      <li><span class="mini"></span><div><small>from <b>joe</b> who likes:</small><p>HELLO WORLD</p></div></li>
      <li><span class="mini"></span><div><small>from <b>joe</b> who likes:</small><p>HELLO WORLD</p></div></li>
      <li><span class="mini"></span><div><small>from <b>johanna</b> who likes:</small><p>A good coffee in the....</p></div></li>
      <li><span class="mini"></span><div><small>from <b>Marry</b> who likes:</small><p>HELLO WORLD</p></div></li>
    </ul>
  </section>
</aside>

<footer class="footer">© 2011 ZestLoop.com</footer>
</body>
</html>
```